Public Adjuster mailing campaign

We are public insurance adjusters. When people (the insured) are not being paid fairly on their insurance claim, we help them get paid all they are owed according to their coverage.We would like a post card mailer to send to homes that have been damaged by a recent tornado. I would like to say something like...Storm Damage?Is your insurance paying everything you are owed?You have rights!Get a FREE claim review!CALL NOW!972-954-6845ADJUSTER FOR THE INSUREDI would like to see a photo in the back ground of a damaged home. I would like a design on both sides of the post card.Colors I prefer are navy as a base color and white text ( or red text for the CALL NOW and the phone number.I would like the message to communicate I am a licensed public adjuster working for the insured and I can help them get what they are owed from the insurance company.

```html
<!DOCTYPE html>
<html lang="en">
<head>
<meta charset="utf-8">
<title>Storm Damage Postcard</title>
<link rel="stylesheet" href="https://fonts.googleapis.com/css2?family=Oswald:wght@500;600;700&family=Didact+Gothic&display=swap">
<style>
  :root {
    --navy: #243d8c;
    --red: #d71f27;
    --white: #ffffff;
    --sky: #b7c3e6;
    --haze: #c7c3d3;
    --debris: #c9b8aa;
  }
  html, body {
    margin: 0;
    padding: 0;
    width: 1200px;
    height: 851px;
    overflow: hidden;
    background: var(--white);
  }
  .postcard {
    position: relative;
    width: 1200px;
    height: 851px;
    overflow: hidden;
    font-family: "Oswald", sans-serif;
  }
  .backdrop {
    position: absolute;
    inset: 0;
    background: linear-gradient(180deg, var(--sky) 0%, #bfc6e2 35%, var(--haze) 52%, #cbbcb3 70%, var(--debris) 100%);
  }
  .band {
    position: absolute;
    top: 0;
    height: 851px;
    width: 82px;
    background: var(--navy);
  }
  .band::after {
    content: "";
    position: absolute;
    top: 0;
    bottom: 0;
    left: 39px;
    width: 4px;
    background: var(--white);
  }
  .band--left { left: 52px; }
  .band--right { left: 1064px; }
  .line {
    position: absolute;
    left: 0;
    width: 1200px;
    margin: 0;
    text-align: center;
    line-height: 1;
    white-space: nowrap;
  }
  .headline {
    top: 92px;
    font-size: 72px;
    font-weight: 700;
    color: var(--white);
    -webkit-text-stroke: 2px var(--navy);
    letter-spacing: 1px;
  }
  .question {
    top: 196px;
    font-family: "Didact Gothic", sans-serif;
    font-size: 26px;
    line-height: 43px;
    color: var(--white);
    font-weight: 700;
  }
  .rights {
    top: 304px;
    font-size: 42px;
    font-weight: 600;
    color: var(--navy);
  }
  .rule {
    position: absolute;
    left: 309px;
    width: 581px;
    height: 3px;
    background: var(--navy);
  }
  .rule--top { top: 403px; }
  .rule--bottom { top: 698px; }
  .offer {
    top: 446px;
    font-size: 32px;
    font-weight: 600;
    color: var(--red);
  }
  .call {
    top: 516px;
    font-size: 62px;
    font-weight: 700;
    color: var(--red);
  }
  .phone {
    top: 603px;
    font-size: 64px;
    font-weight: 700;
    color: var(--red);
  }
  .tagline {
    top: 742px;
    font-size: 42px;
    font-weight: 600;
    color: var(--navy);
  }
</style>
</head>
<body>
  <main class="postcard">
    <div class="backdrop" role="img" aria-label="Photo of a tornado-damaged house with its roof torn off and debris scattered across the yard, washed in a pale blue tint"></div>
    <div class="band band--left"></div>
    <div class="band band--right"></div>

    <h1 class="line headline">STORM DAMAGE?</h1>
    <p class="line question">Is your insurance paying everything<br>you are owned?</p>
    <p class="line rights">YOU HAVE RIGHTS!</p>
    <div class="rule rule--top"></div>
    <p class="line offer">Get a FREE claim review!</p>
    <p class="line call">CALL NOW!</p>
    <p class="line phone">815-372-4091</p>
    <div class="rule rule--bottom"></div>
    <p class="line tagline">ADJUSTER FOR THE INSURED</p>
  </main>
</body>
</html>
```